Alaska Law Firm Needs a Sticker Design

We need a design for stickers to put on already-printed brochures. We mail the brochures to potential clients so they can learn more about accident-induced injuries, insurance claims, legal representation, and our own law firm.

One of our lawyers wrote a book that provides a helpful overview of personal injury claims. We are offering this book for free to anyone who calls and requests it. Therefore, the sticker design should include one of the following phrases, or something very similar:
a) "Still have questions? Call and request our book-- for free!"
b) "Still have questions about auto accident claims? Call and request our book today."
c) "Still have questions about filing a claim? Call and request a free copy of our book."
d) "Still have questions? Call us today to request a free copy of our book, Clear Lanes Ahead."
e) "To learn more about automobile accidents and insurance, call today and request a free copy of our book."

The sticker should be approximately 3"x3" and may be a circle, square, rectangle, or ellipsis. The sticker will be placed on the back of the folder, which is light blue. We would like the sticker to match the color scheme of our website and the folder.

I will upload an image of the book cover as soon as I obtain it.

Industry/Entity Type

Law Firm

Font styles to use
Serif
Sans Serif

Requirements
Should not have
• Bright colors that aren't already used in the folder design. e.g. no bright orange, pink, chartreuse, turquoise, yellow, red.

```html
<!DOCTYPE html>
<html lang="en">
<head>
<meta charset="utf-8">
<title>Book Offer Sticker Concepts</title>
<link rel="stylesheet" href="https://fonts.googleapis.com/css2?family=Roboto+Condensed:wght@700&family=Arimo:wght@700&display=swap">
<style>
  :root {
    --canvas-bg: #ffffff;
    --frame-line: #4a4a4a;
    --folder-blue: #cfe2f3;
    --ink: #13202e;
    --headline-white: #ffffff;
    --tone-navy: #1f3b5c;
    --tone-periwinkle: #7f95c8;
    --tone-sage: #5f6f5a;
    --tone-slate: #3e6a7c;
    --tone-steel: #4a5a70;
  }
  html, body {
    margin: 0;
    padding: 0;
    overflow: hidden;
    background: var(--canvas-bg);
  }
  .board {
    position: relative;
    width: 1200px;
    height: 801px;
    box-sizing: border-box;
    border: 1px solid var(--frame-line);
    background: var(--canvas-bg);
    overflow: hidden;
  }
  .sticker {
    position: absolute;
    width: 342.4px;
    height: 342.4px;
    display: block;
  }
  .sticker--navy { left: 29.6px; top: 29.6px; }
  .sticker--periwinkle { left: 428.8px; top: 29.6px; }
  .sticker--sage { left: 828px; top: 29.6px; }
  .sticker--slate { left: 29.6px; top: 428.8px; }
  .sticker--steel { left: 428.8px; top: 428.8px; }

  .sticker--navy .sticker__field { fill: var(--tone-navy); }
  .sticker--periwinkle .sticker__field { fill: var(--tone-periwinkle); }
  .sticker--sage .sticker__field { fill: var(--tone-sage); }
  .sticker--slate .sticker__field { fill: var(--tone-slate); }
  .sticker--steel .sticker__field { fill: var(--tone-steel); }

  .sticker__wave { fill: var(--folder-blue); stroke: var(--ink); stroke-width: 4; }
  .sticker__band { fill: var(--folder-blue); }
  .sticker__base { stroke: var(--ink); stroke-width: 3.5; }
  .phone__outline { fill: none; stroke: var(--ink); stroke-width: 22; stroke-linecap: round; stroke-linejoin: round; }
  .phone__inner { fill: none; stroke: var(--folder-blue); stroke-width: 13; stroke-linecap: round; stroke-linejoin: round; }
  .signal__outline { fill: none; stroke: var(--ink); stroke-width: 16; stroke-linecap: round; }
  .signal__inner { fill: none; stroke: var(--folder-blue); stroke-width: 8; stroke-linecap: round; }

  .headline {
    font-family: "Roboto Condensed", "Arial Narrow", sans-serif;
    font-weight: 700;
    fill: var(--headline-white);
    text-anchor: middle;
  }
  .headline--lead { font-size: 42px; }
  .headline--lead-small { font-size: 35px; }
  .headline--big { font-size: 72px; }
  .headline--big-tight { font-size: 68px; }
  .offer {
    font-family: "Arimo", Arial, sans-serif;
    font-weight: 700;
    fill: var(--ink);
    text-anchor: middle;
  }
  .offer--regular { font-size: 27.5px; }
  .offer--compact { font-size: 21.5px; }
</style>
</head>
<body>
<div class="board">

  <svg class="sticker sticker--navy" viewBox="0 0 428 428" aria-label="Still have questions? Call and request our book for free!">
    <rect class="sticker__field" width="428" height="428"/>
    <path class="sticker__wave" d="M0,262 Q120,228 236,282 Q320,172 428,182 L428,428 L0,428 Z"/>
    <rect class="sticker__band" x="0" y="395" width="428" height="33"/>
    <line class="sticker__base" x1="0" y1="393" x2="428" y2="393"/>
    <g class="phone">
      <path class="signal__outline" d="M282,340 C278,300 305,278 342,282"/>
      <path class="signal__inner" d="M282,340 C278,300 305,278 342,282"/>
      <path class="signal__outline" d="M304,343 C302,320 316,305 338,307"/>
      <path class="signal__inner" d="M304,343 C302,320 316,305 338,307"/>
      <path class="phone__outline" d="M378,300 C405,295 420,330 400,362 C385,385 360,393 322,392"/>
      <path class="phone__inner" d="M378,300 C405,295 420,330 400,362 C385,385 360,393 322,392"/>
    </g>
    <text class="headline headline--lead" x="213" y="96">Still Have</text>
    <text class="headline headline--big" x="213" y="168">Questions?</text>
    <text class="offer offer--regular" x="131" y="318">Call And</text>
    <text class="offer offer--regular" x="131" y="352">Request Our</text>
    <text class="offer offer--regular" x="131" y="386">Book-for Free!</text>
  </svg>

  <svg class="sticker sticker--periwinkle" viewBox="0 0 428 428" aria-label="Still have questions about auto accident claims? Call and request our book for free!">
    <rect class="sticker__field" width="428" height="428"/>
    <path class="sticker__wave" d="M0,262 Q120,228 236,282 Q320,172 428,182 L428,428 L0,428 Z"/>
    <rect class="sticker__band" x="0" y="395" width="428" height="33"/>
    <line class="sticker__base" x1="0" y1="393" x2="428" y2="393"/>
    <g class="phone">
      <path class="signal__outline" d="M282,340 C278,300 305,278 342,282"/>
      <path class="signal__inner" d="M282,340 C278,300 305,278 342,282"/>
      <path class="signal__outline" d="M304,343 C302,320 316,305 338,307"/>
      <path class="signal__inner" d="M304,343 C302,320 316,305 338,307"/>
      <path class="phone__outline" d="M378,300 C405,295 420,330 400,362 C385,385 360,393 322,392"/>
      <path class="phone__inner" d="M378,300 C405,295 420,330 400,362 C385,385 360,393 322,392"/>
    </g>
    <text class="headline headline--lead" x="213" y="64">Still Have Questions</text>
    <text class="headline headline--lead" x="213" y="107">About Auto Accident</text>
    <text class="headline headline--big" x="213" y="178">Claims?</text>
    <text class="offer offer--regular" x="131" y="318">Call And</text>
    <text class="offer offer--regular" x="131" y="352">Request Our</text>
    <text class="offer offer--regular" x="131" y="386">Book-for Free!</text>
  </svg>

  <svg class="sticker sticker--sage" viewBox="0 0 428 428" aria-label="Still have questions about filing a claim? Call and request a free copy of our book.">
    <rect class="sticker__field" width="428" height="428"/>
    <path class="sticker__wave" d="M0,262 Q120,228 236,282 Q320,172 428,182 L428,428 L0,428 Z"/>
    <rect class="sticker__band" x="0" y="395" width="428" height="33"/>
    <line class="sticker__base" x1="0" y1="393" x2="428" y2="393"/>
    <g class="phone">
      <path class="signal__outline" d="M282,340 C278,300 305,278 342,282"/>
      <path class="signal__inner" d="M282,340 C278,300 305,278 342,282"/>
      <path class="signal__outline" d="M304,343 C302,320 316,305 338,307"/>
      <path class="signal__inner" d="M304,343 C302,320 316,305 338,307"/>
      <path class="phone__outline" d="M378,300 C405,295 420,330 400,362 C385,385 360,393 322,392"/>
      <path class="phone__inner" d="M378,300 C405,295 420,330 400,362 C385,385 360,393 322,392"/>
    </g>
    <text class="headline headline--lead" x="213" y="64">Still Have Questions</text>
    <text class="headline headline--lead" x="213" y="107">About Filing a</text>
    <text class="headline headline--big" x="213" y="178">Claims?</text>
    <text class="offer offer--regular" x="146" y="315">Call And Request</text>
    <text class="offer offer--regular" x="146" y="348">A Free Copy Of</text>
    <text class="offer offer--regular" x="146" y="381">Our Book.</text>
  </svg>

  <svg class="sticker sticker--slate" viewBox="0 0 428 428" aria-label="Still have questions? Call us today to request a free copy of our book, Clear Lanes Ahead.">
    <rect class="sticker__field" width="428" height="428"/>
    <path class="sticker__wave" d="M0,262 Q120,228 236,282 Q320,172 428,182 L428,428 L0,428 Z"/>
    <rect class="sticker__band" x="0" y="395" width="428" height="33"/>
    <line class="sticker__base" x1="0" y1="393" x2="428" y2="393"/>
    <g class="phone">
      <path class="signal__outline" d="M282,340 C278,300 305,278 342,282"/>
      <path class="signal__inner" d="M282,340 C278,300 305,278 342,282"/>
      <path class="signal__outline" d="M304,343 C302,320 316,305 338,307"/>
      <path class="signal__inner" d="M304,343 C302,320 316,305 338,307"/>
      <path class="phone__outline" d="M378,300 C405,295 420,330 400,362 C385,385 360,393 322,392"/>
      <path class="phone__inner" d="M378,300 C405,295 420,330 400,362 C385,385 360,393 322,392"/>
    </g>
    <text class="headline headline--lead" x="213" y="96">Still Have</text>
    <text class="headline headline--big" x="213" y="168">Questions?</text>
    <text class="offer offer--compact" x="139" y="304">Call Us Today To</text>
    <text class="offer offer--compact" x="139" y="330">Request A Free Copy</text>
    <text class="offer offer--compact" x="139" y="355">Of Our Book,</text>
    <text class="offer offer--compact" x="139" y="381">Clear Lanes Ahead.</text>
  </svg>

  <svg class="sticker sticker--steel" viewBox="0 0 428 428" aria-label="To learn more about automobile accidents and insurance? Call and request our book for free!">
    <rect class="sticker__field" width="428" height="428"/>
    <path class="sticker__wave" d="M0,262 Q120,228 236,282 Q320,172 428,182 L428,428 L0,428 Z"/>
    <rect class="sticker__band" x="0" y="395" width="428" height="33"/>
    <line class="sticker__base" x1="0" y1="393" x2="428" y2="393"/>
    <g class="phone">
      <path class="signal__outline" d="M282,340 C278,300 305,278 342,282"/>
      <path class="signal__inner" d="M282,340 C278,300 305,278 342,282"/>
      <path class="signal__outline" d="M304,343 C302,320 316,305 338,307"/>
      <path class="signal__inner" d="M304,343 C302,320 316,305 338,307"/>
      <path class="phone__outline" d="M378,300 C405,295 420,330 400,362 C385,385 360,393 322,392"/>
      <path class="phone__inner" d="M378,300 C405,295 420,330 400,362 C385,385 360,393 322,392"/>
    </g>
    <text class="headline headline--lead-small" x="213" y="59">To Learn More About</text>
    <text class="headline headline--lead-small" x="213" y="100">Automobile Accidents And</text>
    <text class="headline headline--big-tight" x="213" y="170">Insurance?</text>
    <text class="offer offer--regular" x="131" y="318">Call And</text>
    <text class="offer offer--regular" x="131" y="352">Request Our</text>
    <text class="offer offer--regular" x="131" y="386">Book-for Free!</text>
  </svg>

</div>
</body>
</html>
```